Saltwater Aquarium Store Business Cards

Im looking for a fresh new look to my out dated business cards for my company. Its a retail saltwater aquarium store. I want like a modern design that has an aquatic underwater feel. Needs to have certain business information as well. I would like to incorporate my logo as well. and a qr code for our website.
Logo Text
already have a logo

```html
<!DOCTYPE html>
<html lang="en">
<head>
<meta charset="utf-8">
<title>Blue Reef Outfitters – Business Cards</title>
<link rel="stylesheet" href="https://fonts.googleapis.com/css2?family=Lato:wght@400;700;900&display=swap">
<style>
  :root {
    --stage: #2b2b2b;
    --ink-dark: #0f2a3d;
    --brand-blue: #2a9bd8;
    --brand-red: #e8484f;
    --text-grey: #2c2f33;
    --deep-1: #0b2238;
    --deep-2: #153a5a;
    --deep-3: #0a1a2b;
    --aqua-1: #7fe0f0;
    --aqua-2: #1fa3c4;
    --aqua-3: #0f6a8c;
    --white: #ffffff;
  }
  * { box-sizing: border-box; margin: 0; padding: 0; }
  html, body {
    width: 1200px; height: 875px; overflow: hidden;
    background: var(--stage);
    font-family: "Lato", Arial, sans-serif;
  }
  .stage {
    width: 1200px; height: 875px;
    display: flex; flex-direction: column; align-items: center; justify-content: center;
    gap: 40px;
  }
  .card {
    width: 620px; height: 354px; border-radius: 22px;
    position: relative; overflow: hidden;
    box-shadow: 0 18px 40px rgba(0,0,0,.45);
  }
  /* Back card */
  .card--back .scene {
    position: absolute; inset: 0;
    background:
      radial-gradient(ellipse at 40% 0%, rgba(70,130,180,.35), transparent 60%),
      linear-gradient(180deg, var(--deep-2) 0%, var(--deep-1) 55%, var(--deep-3) 100%);
  }
  .card--back .brand {
    position: absolute; left: 0; right: 0; top: 50%; transform: translateY(-50%);
    display: flex; align-items: center; justify-content: center; gap: 16px;
  }
  .brand__mark {
    width: 52px; height: 52px; border-radius: 50%;
    background: var(--brand-blue);
  }
  .card--back .brand__name {
    font-weight: 900; font-size: 46px; color: var(--white); letter-spacing: .5px;
  }
  /* Front card */
  .card--front { background: var(--white); }
  .card--front .scene {
    position: absolute; top: 0; right: 0; width: 330px; height: 100%;
    background:
      radial-gradient(circle at 62% 55%, var(--aqua-1) 0%, var(--aqua-2) 45%, var(--aqua-3) 80%);
  }
  .card--front .scene::after {
    content: ""; position: absolute; inset: 0;
    background: linear-gradient(90deg, var(--white) 0%, rgba(255,255,255,0) 45%);
  }
  .details {
    position: absolute; left: 40px; top: 44px;
  }
  .card--front .brand { display: flex; align-items: center; gap: 12px; }
  .card--front .brand__mark { width: 40px; height: 40px; }
  .card--front .brand__name {
    font-weight: 900; font-size: 30px; color: var(--ink-dark);
  }
  .person { margin-top: 26px; }
  .person__name {
    font-weight: 900; font-size: 34px; color: var(--brand-blue); letter-spacing: .5px;
  }
  .person__role { font-size: 20px; color: var(--brand-red); margin-top: 2px; }
  .contact { list-style: none; margin-top: 20px; }
  .contact li {
    display: flex; align-items: flex-start; gap: 12px;
    font-size: 15px; color: var(--text-grey); line-height: 1.3; margin-bottom: 5px;
  }
  .contact svg { width: 14px; height: 14px; flex: none; margin-top: 2px; fill: var(--brand-red); }
</style>
</head>
<body>
<main class="stage">
  <section class="card card--back">
    <div class="scene" role="img" aria-label="Dark deep-sea reef scene with rocks and light rays"></div>
    <div class="brand">
      <span class="brand__mark"></span>
      <span class="brand__name">Blue Reef Outfitters</span>
    </div>
  </section>

  <section class="card card--front">
    <div class="scene" role="img" aria-label="Round aquarium bowl with coral and tropical fish"></div>
    <div class="details">
      <div class="brand">
        <span class="brand__mark"></span>
        <span class="brand__name">Blue Reef Outfitters</span>
      </div>
      <div class="person">
        <div class="person__name">DANIEL HARPER</div>
        <div class="person__role">Founder &amp; CEO</div>
      </div>
      <ul class="contact">
        <li>
          <svg viewBox="0 0 24 24"><path d="M12 2a7 7 0 0 0-7 7c0 5 7 13 7 13s7-8 7-13a7 7 0 0 0-7-7zm0 9.5A2.5 2.5 0 1 1 12 6.5a2.5 2.5 0 0 1 0 5z"/></svg>
          <span>Your Address, City<br>State, Country, Zip 1235</span>
        </li>
        <li>
          <svg viewBox="0 0 24 24"><path d="M6.6 10.8a15 15 0 0 0 6.6 6.6l2.2-2.2a1 1 0 0 1 1-.25 11.4 11.4 0 0 0 3.6.6 1 1 0 0 1 1 1V20a1 1 0 0 1-1 1A17 17 0 0 1 3 4a1 1 0 0 1 1-1h3.5a1 1 0 0 1 1 1c0 1.25.2 2.45.6 3.6a1 1 0 0 1-.25 1z"/></svg>
          <span>(123) 456-7890</span>
        </li>
        <li>
          <svg viewBox="0 0 24 24"><path d="M2 5h20v14H2zm2 2v.5l8 5 8-5V7z"/></svg>
          <span>store@bluereefoutfitters.com</span>
        </li>
        <li>
          <svg viewBox="0 0 24 24"><path d="M12 2a10 10 0 1 0 0 20 10 10 0 0 0 0-20zm0 2c.9 1.2 1.6 2.8 1.9 4.5h-3.8C10.4 6.8 11.1 5.2 12 4zM4.3 13a8 8 0 0 1 0-2h3.5a16 16 0 0 0 0 2zm.8 2h3c.3 1.4.8 2.7 1.5 3.8A8 8 0 0 1 5.1 15zm3-6h-3a8 8 0 0 1 4.5-3.8C8.9 6.3 8.4 7.6 8.1 9zM12 20c-.9-1.2-1.6-2.8-1.9-5h3.8c-.3 2.2-1 3.8-1.9 5zm2.2-7H9.8a14 14 0 0 1 0-2h4.4a14 14 0 0 1 0 2zm.2 5.8c.7-1.1 1.2-2.4 1.5-3.8h3a8 8 0 0 1-4.5 3.8zM16.2 13a16 16 0 0 0 0-2h3.5a8 8 0 0 1 0 2zm-.3-4c-.3-1.4-.8-2.7-1.5-3.8A8 8 0 0 1 18.9 9z"/></svg>
          <span>bluereefoutfitters.com</span>
        </li>
      </ul>
    </div>
  </section>
</main>
</body>
</html>
```